Landing Page für Persönlichkeitsquiz
Zielgruppe
Persönlichkeitsquiz für Menschen über 40 Jahren die bessere Entscheidungen treffen möchten.
Aufgabenstellung
Landinpage Design plus QUIZ ( 6 Schritte)
Vollständige Projektbeschreibung:
Projektbeschreibung
„Roaming Sideways QUIZ“
roamingsideways.example
- Responsive Design für mobile & website (Most users: mobile)
- Design wird Grundlage für spätere Website
Dieses Quiz wendet sich an Menschen über 40 Jahre, die ihre persönlichen Lebensziele besser erreichen möchten. Bitte denke daran, dass Menschen in unserem Alter schon schlechter sehen – also bitte eine gut lesbare & etwas größere Schrift verwenden!
Auftrag:
QUIZ mit mehreren Runden
Schritte des Quiz:
1. Landingpage
1.1 Video (youtube eingebunden)
1.2 Text
1.3 „Start Quiz“ Button
1.4 „Bekannt aus“ mit Logos von Medien in denen Marv Olden besprochen wurde.
1.5 Testimonials?
QUIZ (Popup)
2. Erste Runde: „Kille“ alle Antworten die Dich nicht interessieren. Total 64 Antworten.
2.1 Text mit Aufgabenbeschreibung „Kille“ alle Antworten die Dich nicht interessieren. Du hast zwei Minuten.“
2.2 Ein Button pro Antwort (wie bei Lernivo)
2.3 Zwei Buttons pro Reihe
2.4 Oben: Progress bar
2.5 Oben: Countdown clock, Restzeit: 2 Minuten
3. Zweite Runde: „Wähle max. 18 Antworten aus die überleben sollen.“
3.1 Text mit Aufgabenbeschreibung „Wähle max. 18 Antworten aus die überleben sollen.“
3.2 Ein Button pro Antwort (wie bei Lernivo)
3.3 Zwei Buttons pro Reihe
3.4 Oben: Progress bar
3.5 Oben: Countdown clock, Restzeit: 60 Sekunden
3.6 Zähler der noch verfügbaren Antworten. Hier: Noch 18, noch 17, noch 16.. etc.
4. Dritte Runde: „Nur 9 Antworten dürfen überleben. Go!“
4.1 Text mit „Nur 9 Antworten dürfen überleben. Go!“
4.2 Ein Button pro Antwort (wie bei Lernivo)
4.3 Zwei Buttons pro Reihe
4.4 Oben: Progress bar
4.5 Oben: Countdown clock, Restzeit 45 ..

```html
<!DOCTYPE html>
<html lang="de">
<head>
<meta charset="utf-8">
<title>Roaming Sideways QUIZ – Ergebnis teilen</title>
<link rel="stylesheet" href="https://fonts.googleapis.com/css2?family=Open+Sans:wght@400;600;700&display=swap">
<style>
:root{
  --hero:#34168f;
  --band:#5a36b4;
  --band-2:#5f3bb9;
  --about:#6238bd;
  --footer:#44209f;
  --muted:#7b5fd8;
  --muted-dark:#2a0f7a;
  --white:#ffffff;
  --ink:#333333;
  --grey:#666666;
  --violet:#c36fd6;
  --violet-line:#c77ae0;
  --gold:#e8b53f;
  --gold-dim:#6a3a6e;
  --pink:#f290c8;
  --field:#ececec;
}
*{box-sizing:border-box;margin:0;padding:0}
html,body{width:864px;height:1200px;overflow:hidden}
body{position:relative;font-family:"Open Sans",Arial,sans-serif;background:var(--about);color:var(--ink)}
.abs{position:absolute}

/* page behind the dialog */
.hero{left:0;top:0;width:864px;height:410px;background:linear-gradient(120deg,#3d1a9e,#2f1691)}
.band{left:0;top:410px;width:864px;height:207px;background:var(--band)}
.band-2{left:0;top:617px;width:864px;height:261px;background:var(--band-2)}
.about{left:0;top:878px;width:864px;height:286px;background:var(--about)}
.site-footer{left:0;top:1164px;width:864px;height:36px;background:var(--footer);font-size:8px;color:var(--muted)}
.site-logo{left:63px;top:38px;font-weight:700;font-size:12.5px;line-height:17px;color:var(--muted);letter-spacing:.3px}
.lang{left:718px;top:58px;width:16px;height:16px;border-radius:50%;background:linear-gradient(#222 0 33%,#c0392b 33% 66%,#e0b030 66%);opacity:.55}
.lang-caret{left:740px;top:62px}
.nav-link{left:770px;top:59px;font-size:10px;color:var(--muted)}
.hero-title{left:63px;top:143px;font-size:19px;font-weight:700;line-height:26px;color:var(--muted)}
.hero-text{left:63px;top:205px;font-size:9.5px;line-height:13px;color:var(--muted);width:300px}
.btn-dim{background:var(--gold-dim);color:var(--muted);border-radius:14px;font-weight:700;font-size:9.5px;display:flex;align-items:center;gap:5px;padding-left:10px}
.hero-btn{left:63px;top:260px;width:120px;height:27px}
.deco-panel{left:739px;top:107px;width:61px;height:201px;background:#5a2aa4}
.circle-dark{border-radius:50%;background:#3a1a9b}
.band-arrow{width:13px;height:13px;border-radius:50%;background:var(--gold-dim)}
.band-press{font-weight:700;font-size:12px;color:var(--muted-dark)}
.card{left:63px;top:698px;width:737px;height:111px;background:#6f4bc6;border-bottom:3px solid #7a3bc0}
.avatar{left:75px;top:711px;width:48px;height:48px;border-radius:50%;background:radial-gradient(#8a5a70,#3b2466)}
.card-text{font-size:7.5px;line-height:10.5px;color:var(--muted-dark)}
.start-behind{left:385px;top:834px;width:93px;height:26px;justify-content:center;padding:0}
.about-title{left:0;width:864px;top:901px;text-align:center;font-weight:700;font-size:11px;color:var(--muted-dark)}
.about-rule{left:418px;top:922px;width:29px;height:2px;background:#7a3bc0}
.about-photo{left:113px;top:953px;width:146px;height:146px;border-radius:50%;background:linear-gradient(135deg,#6a5fb8,#3a2a7a)}
.about-dot{left:78px;top:1074px;width:40px;height:40px;border-radius:50%;background:#3d1aa3}
.about-head{left:312px;top:951px;font-weight:700;font-size:11px;color:var(--muted-dark)}
.about-copy{left:312px;top:984px;width:480px;font-size:8px;line-height:10.7px;color:var(--muted-dark)}
.about-copy p{margin-bottom:10.7px}
.about-btn{left:312px;top:1095px;width:93px;height:27px}

/* dialog */
.dialog{left:125px;top:83px;width:614px;height:756px;background:var(--white);border-bottom:3px solid var(--violet-line);box-shadow:0 2px 8px rgba(0,0,0,.2)}
.goal-badge{left:419px;top:70px;width:26px;height:26px;border-radius:50%;background:var(--violet);border:2px solid var(--white);display:flex;align-items:center;justify-content:center}
.back{left:148px;top:100px;display:flex;align-items:center;gap:5px;font-weight:700;font-size:10px;color:var(--gold)}
.dot-gold{width:13px;height:13px;border-radius:50%;background:var(--gold);display:flex;align-items:center;justify-content:center}
.dialog-title{left:0;width:864px;top:99px;text-align:center;font-size:11px;color:var(--grey)}
.close{display:flex;align-items:center;gap:5px;font-weight:700;font-size:10px}
.dialog-close{left:652px;top:99px;color:var(--violet)}
.video{left:148px;top:131px;width:568px;height:159px;background:var(--pink)}
.play{left:418px;top:200px;width:26px;height:26px;border-radius:50%;background:var(--white);display:flex;align-items:center;justify-content:center}
.result-intro{left:148px;top:344px;width:568px;text-align:center;font-size:11px;color:var(--grey)}
.result-copy{left:150px;top:503px;width:564px;text-align:center;font-size:9.5px;line-height:14px;color:var(--grey)}
.field{height:27px;border-radius:14px;background:var(--field);font-size:9.5px;color:var(--grey);padding:0 16px;display:flex;align-items:center}
.field-name{left:148px;top:660px;width:179px}
.field-mail{left:335px;top:660px;width:270px}
.send{left:615px;top:660px;width:93px;height:27px;border-radius:14px;background:var(--gold);color:var(--white);font-weight:700;font-size:9.5px;display:flex;align-items:center;justify-content:center;gap:4px}
.press-title{left:0;width:864px;top:717px;text-align:center;font-weight:700;font-size:11px;color:var(--ink)}
.press-rule{left:418px;top:738px;width:29px;height:2px;background:var(--violet)}
.press-row{left:172px;top:755px;width:520px;height:42px;display:flex;align-items:center;justify-content:space-between}
.press-name{font-weight:700;font-size:12px;color:#000}
.arrow-gold{top:769px}

/* share panel */
.share{left:307px;top:279px;width:250px;height:373px;background:var(--violet);color:var(--white);box-shadow:0 2px 6px rgba(0,0,0,.15)}
.share-head{left:11px;top:10px;font-weight:700;font-size:10.5px}
.share-close{left:179px;top:10px;color:var(--white)}
.share-image{left:11px;top:33px;width:228px;height:119px;background:var(--pink)}
.share-url{left:11px;top:159px;font-size:9px}
.share-lead{left:11px;top:176px;font-weight:700;font-size:10.5px}
.share-text{left:11px;top:195px;font-size:9px;line-height:12.5px}
.share-rule{left:11px;top:227px;width:228px;height:1px;background:#e3b3ee}
.share-list{left:14px;top:236px;list-style:none;font-size:9.5px}
.share-list li{display:flex;align-items:center;gap:7px;height:21px}
.share-mark{width:12px;height:12px;border:1.3px solid var(--white);border-radius:50%}
.copy-label{left:11px;top:320px;font-size:9.5px}
.copy-field{left:11px;top:340px;width:228px;height:20px;background:var(--white);color:var(--grey);font-size:8px;padding:0 6px;display:flex;align-items:center;white-space:nowrap;overflow:hidden}
</style>
</head>
<body>

<!-- page -->
<div class="abs hero"></div>
<div class="abs band"></div>
<div class="abs band-2"></div>
<div class="abs about"></div>

<div class="abs site-logo">ROAMING<br>SIDEWAYS</div>
<div class="abs lang"></div>
<svg class="abs lang-caret" width="9" height="6" viewBox="0 0 9 6"><path d="M1 1l3.5 3.5L8 1" fill="none" stroke="#7b5fd8" stroke-width="1.3"/></svg>
<div class="abs nav-link">Fragen</div>
<div class="abs hero-title">Herzlich willkommen<br>bei Roaming Sideways</div>
<div class="abs hero-text">Lorem ipsum dolor sit amet, consetetur sadipscing elitr, sed diam nonumy eirmod tempor invidunt ut labore et dolore magna aliquyam erat, sed diam voluptua.</div>
<div class="abs btn-dim hero-btn">→ Quiz starten</div>
<div class="abs deco-panel"></div>
<div class="abs circle-dark" style="left:804px;top:430px;width:120px;height:125px"></div>
<div class="abs circle-dark" style="left:-60px;top:655px;width:94px;height:130px"></div>

<div class="abs band-arrow" style="left:63px;top:511px"></div>
<div class="abs band-arrow" style="left:787px;top:511px"></div>
<div class="abs band-press" style="left:84px;top:509px">Quervolt</div>
<div class="abs band-press" style="left:745px;top:509px">Funk</div>

<div class="abs card"></div>
<div class="abs avatar" role="img" aria-label="Porträtfoto einer Person im Freien"></div>
<div class="abs card-text" style="left:75px;top:767px;width:60px">Lorem ipsum sed diam non dolore magna</div>
<div class="abs card-text" style="left:738px;top:767px;width:60px">sadipscing elitr, ut labore et voluptua.</div>
<svg class="abs" style="left:776px;top:707px" width="14" height="14" viewBox="0 0 14 14"><path d="M7 1.5a5.5 5 0 1 1-3 9.2L1.5 12l.9-2.6A5 5 0 0 1 7 1.5z" fill="none" stroke="#2a0f7a" stroke-width="1.1"/></svg>
<div class="abs btn-dim start-behind">→ Quiz starten</div>

<div class="abs about-title">Über MarvOlden</div>
<div class="abs about-rule"></div>
<div class="abs about-photo" role="img" aria-label="Foto von zwei lächelnden Personen"></div>
<div class="abs about-dot"></div>
<div class="abs about-head">Was meine Oma mich lehrte</div>
<div class="abs about-copy">
  <p>Die einflussreichste Person in meinem Leben war meine Großmutter. Sie wurde im Deutschen Kaiserreich geboren; erlebte zwei Weltkriege, die Mondlandung und den ersten Heimcomputer.</p>
  <p>Während des Krieges ging sie nach Dresden, um ihre Tochter aus der “Landverschickung” nach Hause zu holen, und zwang die Schulleiterin, ihre Tochter zurückzugeben. Dann brachte Oma sie (die Tochter, nicht die Schulleiterin) durch halb Deutschland und das ganze Chaos des zerstörten Eisenbahnnetzes nach Hause. Dresden wurde in der nächsten Nacht bombardiert, meine Mutter hätte das nicht überlebt.</p>
  <p>Meine Großmutter lehrte mich, Menschen nach ihren Taten zu beurteilen, nicht nach ihren Worten.</p>
</div>
<div class="abs btn-dim about-btn">→ Quiz starten</div>

<footer class="abs site-footer">
  <span class="abs" style="left:63px;top:13px">© Roaming Sideways QUIZ</span>
  <span class="abs" style="left:633px;top:13px">Impressum</span>
  <span class="abs" style="left:700px;top:13px">Datenschutz</span>
  <span class="abs" style="left:767px;top:13px">Sitemap</span>
</footer>

<!-- result dialog -->
<section class="abs dialog"></section>
<div class="abs goal-badge">
  <svg width="14" height="14" viewBox="0 0 14 14"><path d="M7 1.2l1.7 3.6 3.9.5-2.9 2.7.8 3.9L7 10l-3.5 1.9.8-3.9L1.4 5.3l3.9-.5z" fill="none" stroke="#fff" stroke-width="1.1" stroke-linejoin="round"/></svg>
</div>
<div class="abs back"><span class="dot-gold"><svg width="6" height="7" viewBox="0 0 6 7"><path d="M4.5 1L2 3.5 4.5 6" fill="none" stroke="#fff" stroke-width="1.3"/></svg></span>zurück</div>
<div class="abs dialog-title">Ziel erreicht!</div>
<div class="abs close dialog-close">Schließen <svg width="9" height="9" viewBox="0 0 9 9"><path d="M1 1l7 7M8 1L1 8" stroke="#c36fd6" stroke-width="2"/></svg></div>
<div class="abs video" role="img" aria-label="Video-Vorschau: Illustration mit Auge, Lupe und zeigender Hand auf Rosa"></div>
<div class="abs play"><svg width="10" height="11" viewBox="0 0 10 11"><path d="M2 1l7 4.5L2 10z" fill="#f290c8"/></svg></div>
<div class="abs result-intro">Hier sind Deine Werte – geordnet nach ihrer persönlichen Wichtigkeit.</div>
<div class="abs result-copy">Lorem ipsum dolor sit amet, consetetur sadipscing elitr, sed diam nonumy eirmod tempor invidunt ut labore et dolore magna aliquyam erat, sed diam voluptua. At vero eos et accusam et justo duo dolores. Stet clita kasd gubergren, no sea takimata sanctus est Lorem ipsum dolor sit amet. Lorem ipsum dolor sit amet, consetetur sadipscing elitr, sed diam nonumy eirmod tempor invidunt ut labore et dolore magna aliquyam erat, sed diam voluptua.</div>

<div class="abs field field-name">Deine Name</div>
<div class="abs field field-mail">E-Mail-Adresse</div>
<div class="abs send">→ Jetzt senden</div>

<div class="abs press-title">Bekannt aus</div>
<div class="abs press-rule"></div>
<div class="abs dot-gold arrow-gold" style="left:148px"><svg width="6" height="7" viewBox="0 0 6 7"><path d="M4.5 1L2 3.5 4.5 6" fill="none" stroke="#fff" stroke-width="1.3"/></svg></div>
<div class="abs dot-gold arrow-gold" style="left:703px"><svg width="6" height="7" viewBox="0 0 6 7"><path d="M1.5 1L4 3.5 1.5 6" fill="none" stroke="#fff" stroke-width="1.3"/></svg></div>
<div class="abs press-row">
  <span class="press-name">Quervolt</span>
  <span class="press-name">Heftmond</span>
  <span class="press-name">Sendelux</span>
  <span class="press-name">Zeitraster</span>
  <span class="press-name">Kanalfuchs</span>
  <span class="press-name">Tageskiesel</span>
  <span class="press-name">Funkbrise</span>
</div>

<!-- share panel -->
<aside class="abs share">
  <div class="abs share-head">Teilen</div>
  <div class="abs close share-close">Schließen <svg width="9" height="9" viewBox="0 0 9 9"><path d="M1 1l7 7M8 1L1 8" stroke="#fff" stroke-width="2"/></svg></div>
  <div class="abs share-image" role="img" aria-label="Illustration mit Lupe, Person mit Auge und zeigender Hand auf Rosa"></div>
  <div class="abs share-url">WWW.ROAMINGSIDEWAYS-QUIZ.EXAMPLE</div>
  <div class="abs share-lead">Schau dir das Ergebnis an!</div>
  <div class="abs share-text">Welche Persönlichkeit bist du?<br>Nimm jetzt kostenfrei teil und erfahre es selbst.</div>
  <div class="abs share-rule"></div>
  <ul class="abs share-list">
    <li><span class="share-mark"></span>Kreisnetz</li>
    <li><span class="share-mark"></span>Schnellwort</li>
    <li><span class="share-mark"></span>Momentwand</li>
    <li><svg width="13" height="11" viewBox="0 0 13 11"><rect x=".7" y=".7" width="11.6" height="9.6" rx="1" fill="none" stroke="#fff" stroke-width="1.2"/><path d="M1 1.2l5.5 4.5L12 1.2" fill="none" stroke="#fff" stroke-width="1.2"/></svg>E-Mail</li>
  </ul>
  <div class="abs copy-label">Zum Kopieren des Links klicken</div>
  <div class="abs copy-field">https://roamingsideways-quiz.example/ergebnis/doKkid8</div>
</aside>

</body>
</html>
```